Need Web Design for Business Process Outsourcing Company (Kelmora)

Kelmora is a business process outsourcing company. Need a simple site similar to http://www.tarvenholm.com/ but with a more professional and credible look. New to the process; not sure where to start and comparing my options. Please let me know what my options are if I choose to go with you. Logo is attached for your reference. Please use same colorway

Reason: I want the final product to be coded. Please confirm you will be able to code final design.

Industry/Entity Type

Business

Coding

Coded - Design and coding required

```html
<!DOCTYPE html>
<html lang="en">
<head>
<meta charset="utf-8">
<title>Kelmora — Business Process Outsourcing</title>
<link href="https://fonts.googleapis.com/css2?family=Montserrat:wght@400;600;700&family=Open+Sans:wght@400;600&display=swap" rel="stylesheet">
<style>
:root{
  --blue:#1b8ad8;
  --blue-dark:#0f6fb6;
  --navy:#1d4f7a;
  --ink:#2a2f36;
  --text:#5f6670;
  --muted:#9aa1a9;
  --line:#e4e8ec;
  --soft:#f4f6f8;
  --white:#ffffff;
  --charcoal:#2d3238;
}
*{box-sizing:border-box;margin:0;padding:0}
html,body{width:702px;height:1200px;overflow:hidden;background:var(--white)}
body{font-family:"Open Sans",Arial,sans-serif;color:var(--text);position:relative;font-size:7px}
h1,h2,h3,.brand,.nav a{font-family:"Montserrat",Arial,sans-serif}
section,header,footer{position:absolute;left:0;width:702px}

/* hero */
.hero{top:0;height:232px;overflow:hidden}
.hero-photo{position:absolute;inset:0;background:linear-gradient(160deg,#6f8597 0%,#9fb3c2 35%,#c9d6df 60%,#7d93a5 100%)}
.hero-curve{position:absolute;left:0;bottom:0;width:702px;height:50px}
.contact-strip{position:absolute;left:14px;top:0;width:118px;height:58px;background:var(--blue);color:var(--white);padding:8px 10px;font-size:6.5px;line-height:11px}
.contact-strip .row{display:flex;align-items:center;gap:5px}
.social{display:flex;gap:4px;margin-top:3px}
.social span{width:9px;height:9px;border-radius:50%;background:var(--white);opacity:.85}
.nav{position:absolute;left:150px;top:10px;width:540px;height:34px;background:var(--white);display:flex;align-items:center;padding:0 12px;box-shadow:0 2px 6px rgba(0,0,0,.12)}
.brand{display:flex;align-items:center;gap:5px;font-weight:700;font-size:14px;color:var(--navy)}
.brand .mark{width:12px;height:12px;background:var(--blue)}
.nav ul{list-style:none;display:flex;gap:16px;margin-left:58px}
.nav a{text-decoration:none;font-size:6.5px;color:var(--ink)}
.nav a.active{color:var(--blue);border-bottom:2px solid var(--blue);padding-bottom:3px}
.chat{margin-left:auto;font-size:6px;border:1px solid var(--blue);color:var(--blue);padding:3px 7px;border-radius:2px}
.hero-copy{position:absolute;top:105px;left:0;width:702px;text-align:center;color:var(--white)}
.hero-copy h1{font-size:22px;font-weight:700}
.hero-copy p{font-size:11px;margin-top:3px}
.btn{display:inline-block;background:var(--blue);color:var(--white);font-family:"Montserrat",sans-serif;font-size:6.5px;font-weight:600;padding:5px 12px;border-radius:2px}
.hero-copy .btn{margin-top:10px}
.slide-tab{position:absolute;top:140px;background:var(--blue);color:var(--white);font-size:5.5px;padding:2px 6px}

/* section heading */
.heading{text-align:center}
.heading h2{display:inline-block;font-size:11px;font-weight:600;color:var(--blue);padding:0 22px 5px;border-bottom:2px solid var(--blue)}

/* services */
.services{top:240px;height:340px}
.service-grid{width:360px;margin:22px auto 0;display:grid;grid-template-columns:repeat(3,1fr);gap:10px 10px}
.service{height:128px;text-align:center;padding:16px 10px 0;position:relative}
.service.featured{box-shadow:0 3px 12px rgba(0,0,0,.14);border:1px solid var(--line)}
.service svg{width:22px;height:22px}
.service h3{font-size:7.5px;font-weight:600;color:var(--ink);margin-top:8px}
.service p{font-size:5.5px;line-height:8px;margin-top:8px;color:var(--muted)}
.service .more{position:absolute;left:50%;bottom:14px;margin-left:-5px;width:10px;height:10px;border-radius:50%;background:var(--blue)}

/* who we are */
.about{top:586px;height:150px;background:var(--blue)}
.about .tab{position:absolute;left:311px;top:-8px;width:80px;height:20px;background:var(--white);color:var(--blue);font-family:"Montserrat",sans-serif;font-weight:600;font-size:9px;display:flex;align-items:center;justify-content:center}
.pillars{position:absolute;top:42px;left:152px;width:398px;display:flex;gap:10px}
.pillar{flex:1;height:70px;background:var(--white);display:flex;flex-direction:column}
.pillar .icon{flex:1;display:flex;align-items:center;justify-content:center}
.pillar .label{height:18px;background:var(--navy);color:var(--white);font-size:6px;display:flex;align-items:center;justify-content:center}
.pillar.active{background:var(--navy)}
.pillar.active .label{background:#163d60}

/* news */
.news{top:750px;height:212px}
.news-grid{width:380px;margin:18px auto 0;display:flex;gap:12px}
.post{flex:1;border:1px solid var(--line);height:160px;background:var(--white)}
.post .thumb{height:58px;position:relative}
.post .date{position:absolute;left:10px;bottom:-5px;background:var(--blue);color:var(--white);font-size:5px;padding:2px 6px}
.post h3{font-size:7px;font-weight:600;color:var(--ink);text-align:center;margin-top:12px;line-height:9px}
.post p{font-size:5.3px;line-height:7.5px;text-align:center;margin:5px 10px 0;color:var(--muted)}
.post .meta{display:flex;justify-content:space-between;margin:7px 10px 0;padding-top:4px;border-top:1px solid var(--line);font-size:4.8px;color:var(--muted)}
.post .read{font-size:5.5px;color:var(--ink);margin:6px 10px 0;font-weight:600}

/* call to action */
.cta{top:970px;height:40px;background:var(--charcoal)}
.cta-inner{position:absolute;left:0;top:0;width:460px;height:40px;background:var(--blue);clip-path:polygon(0 0,100% 0,94% 100%,0 100%);padding:8px 0 0 142px;color:var(--white);font-family:"Montserrat",sans-serif;font-weight:600;font-size:7px;line-height:10px}
.cta .btn{position:absolute;left:430px;top:12px;background:var(--blue)}

/* contact */
.contact{top:1020px;height:92px}
.contact-items{width:380px;margin:16px auto 0;display:flex;justify-content:space-between}
.item{display:flex;align-items:center;gap:7px;font-size:6px;line-height:9px;color:var(--text)}
.item svg{width:24px;height:26px}
.item strong{color:var(--ink);font-weight:600}

/* footer */
.site-footer{top:1112px;height:88px;background:var(--soft);border-top:1px solid var(--line)}
.footer-main{position:absolute;top:22px;left:70px;width:562px;display:flex;align-items:center}
.footer-main .brand{font-size:15px}
.footer-links{display:flex;gap:12px;margin-left:50px;list-style:none}
.footer-links li{font-size:6px;color:var(--ink)}
.footer-social{margin-left:auto;display:flex;gap:5px}
.footer-social span{width:11px;height:11px;border-radius:50%;background:var(--ink)}
.copyright{position:absolute;left:0;bottom:0;width:702px;height:20px;background:var(--white);border-top:1px solid var(--line);font-size:5.5px;padding:6px 70px;color:var(--muted)}
</style>
</head>
<body>

<header class="hero">
  <div class="hero-photo" role="img" aria-label="Upward view of glass office towers against the sky"></div>
  <svg class="hero-curve" viewBox="0 0 702 50" preserveAspectRatio="none"><path d="M0 50 L0 10 Q351 70 702 10 L702 50 Z" fill="#fff"/></svg>

  <div class="contact-strip">
    <div class="row">&#9742; +1 (555) 481-2960</div>
    <div class="row">&#9993; hello@kelmora.com</div>
    <div class="social"><span></span><span></span><span></span></div>
  </div>

  <nav class="nav">
    <div class="brand"><span class="mark"></span>Kelmora</div>
    <ul>
      <li><a class="active" href="#">Home</a></li>
      <li><a href="#">Services</a></li>
      <li><a href="#">Solutions</a></li>
      <li><a href="#">Our Experience</a></li>
      <li><a href="#">News</a></li>
      <li><a href="#">Contact Us</a></li>
    </ul>
    <span class="chat">Live Chat</span>
  </nav>

  <span class="slide-tab" style="left:30px">Previous</span>
  <span class="slide-tab" style="right:30px">Next</span>

  <div class="hero-copy">
    <h1>Grow Your Business</h1>
    <p>But I must explain to you how all this mistaken idea</p>
    <span class="btn">Learn More</span>
  </div>
</header>

<section class="services">
  <div class="heading"><h2>Our Services</h2></div>
  <div class="service-grid">
    <div class="service">
      <svg viewBox="0 0 24 24"><circle cx="12" cy="9" r="6" fill="none" stroke="#1b8ad8" stroke-width="2"/><path d="M4 22c1-5 15-5 16 0" fill="none" stroke="#1b8ad8" stroke-width="2"/></svg>
      <h3>Customer Service</h3>
      <p>Sed ut perspiciatis unde omnis iste natus error sit voluptatem accusantium</p>
      <span class="more"></span>
    </div>
    <div class="service featured">
      <svg viewBox="0 0 24 24"><path d="M2 4h4l3 11h11l2-8H7" fill="none" stroke="#1b8ad8" stroke-width="2"/><circle cx="10" cy="20" r="1.8" fill="#1b8ad8"/><circle cx="18" cy="20" r="1.8" fill="#1b8ad8"/></svg>
      <h3>Ecommerce</h3>
      <p>Sed ut perspiciatis unde omnis iste natus error sit voluptatem accusantium</p>
      <span class="more"></span>
    </div>
    <div class="service">
      <svg viewBox="0 0 24 24"><rect x="3" y="5" width="15" height="15" fill="none" stroke="#1b8ad8" stroke-width="2"/><path d="M10 14l10-10" stroke="#1b8ad8" stroke-width="2.5"/></svg>
      <h3>Creative</h3>
      <p>Sed ut perspiciatis unde omnis iste natus error sit voluptatem accusantium</p>
      <span class="more"></span>
    </div>
    <div class="service">
      <svg viewBox="0 0 24 24"><path d="M8 14a6 6 0 1 1 8 0v3H8z" fill="none" stroke="#1b8ad8" stroke-width="2"/><path d="M9 21h6" stroke="#1b8ad8" stroke-width="2"/></svg>
      <h3>IT Solutions</h3>
      <p>Sed ut perspiciatis unde omnis iste natus error sit voluptatem accusantium</p>
      <span class="more"></span>
    </div>
    <div class="service">
      <svg viewBox="0 0 24 24"><circle cx="8" cy="8" r="3.5" fill="#1b8ad8"/><circle cx="17" cy="8" r="3.5" fill="#1b8ad8"/><path d="M2 20c0-5 12-5 12 0M11 20c0-5 12-5 12 0" fill="#1b8ad8"/></svg>
      <h3>Human Resources</h3>
      <p>Sed ut perspiciatis unde omnis iste natus error sit voluptatem accusantium</p>
      <span class="more"></span>
    </div>
    <div class="service">
      <svg viewBox="0 0 24 24"><circle cx="12" cy="12" r="9" fill="none" stroke="#1b8ad8" stroke-width="2"/><path d="M3 12h18M12 3c4 4 4 14 0 18M12 3c-4 4-4 14 0 18" fill="none" stroke="#1b8ad8" stroke-width="1.5"/></svg>
      <h3>Outsourcing</h3>
      <p>Sed ut perspiciatis unde omnis iste natus error sit voluptatem accusantium</p>
      <span class="more"></span>
    </div>
  </div>
</section>

<section class="about">
  <div class="tab">Who We Are</div>
  <div class="pillars">
    <div class="pillar">
      <div class="icon"><svg width="24" height="24" viewBox="0 0 24 24"><path d="M4 21V7h7v14M11 21V3h9v18" fill="none" stroke="#1d4f7a" stroke-width="2"/></svg></div>
      <div class="label">Our Company</div>
    </div>
    <div class="pillar active">
      <div class="icon"><svg width="24" height="24" viewBox="0 0 24 24"><path d="M12 3l3 6 6 1-4.5 4 1 6-5.5-3-5.5 3 1-6L3 10l6-1z" fill="#fff"/></svg></div>
      <div class="label">Our Culture</div>
    </div>
    <div class="pillar">
      <div class="icon"><svg width="24" height="24" viewBox="0 0 24 24"><circle cx="12" cy="8" r="4" fill="#1d4f7a"/><path d="M4 21c1-7 15-7 16 0z" fill="#1d4f7a"/></svg></div>
      <div class="label">Our People</div>
    </div>
    <div class="pillar">
      <div class="icon"><svg width="24" height="24" viewBox="0 0 24 24"><path d="M3 5h8v15H3zM13 5h8v15h-8z" fill="none" stroke="#1d4f7a" stroke-width="2"/></svg></div>
      <div class="label">Our Story</div>
    </div>
    <div class="pillar">
      <div class="icon"><svg width="24" height="24" viewBox="0 0 24 24"><path d="M3 21V10l6-4v4l6-4v4l6-4v15z" fill="none" stroke="#1d4f7a" stroke-width="2"/></svg></div>
      <div class="label">Our Facilities</div>
    </div>
  </div>
</section>

<section class="news">
  <div class="heading"><h2>Latest News</h2></div>
  <div class="news-grid">
    <article class="post">
      <div class="thumb" role="img" aria-label="Team reviewing charts at an office desk" style="background:linear-gradient(135deg,#b9c8d4,#e8edf1)"><span class="date">12 Jan 2024</span></div>
      <h3>The standard Lorem<br>Ipsum passage</h3>
      <p>There are many variations of passages of lorem ipsum available for your reading today</p>
      <div class="meta"><span>By Admin</span><span>24 Likes</span><span>8 Comments</span></div>
      <div class="read">Read More &rsaquo;</div>
    </article>
    <article class="post">
      <div class="thumb" role="img" aria-label="Business partners in a meeting room" style="background:linear-gradient(135deg,#4d5866,#a3adb8)"><span class="date">09 Jan 2024</span></div>
      <h3>The standard Lorem<br>Ipsum passage</h3>
      <p>There are many variations of passages of lorem ipsum available for your reading today</p>
      <div class="meta"><span>By Admin</span><span>18 Likes</span><span>5 Comments</span></div>
      <div class="read">Read More &rsaquo;</div>
    </article>
    <article class="post">
      <div class="thumb" role="img" aria-label="Colleagues working together at laptops" style="background:linear-gradient(135deg,#6b7784,#c4ccd4)"><span class="date">04 Jan 2024</span></div>
      <h3>The standard Lorem<br>Ipsum passage</h3>
      <p>There are many variations of passages of lorem ipsum available for your reading today</p>
      <div class="meta"><span>By Admin</span><span>31 Likes</span><span>12 Comments</span></div>
      <div class="read">Read More &rsaquo;</div>
    </article>
  </div>
</section>

<section class="cta">
  <div class="cta-inner">Passionate About Engaging With Clients And<br>Growing Businesses!</div>
  <span class="btn">Learn More</span>
</section>

<section class="contact">
  <div class="heading"><h2>Contact Us</h2></div>
  <div class="contact-items">
    <div class="item">
      <svg viewBox="0 0 24 26"><path d="M12 1l11 6v12l-11 6-11-6V7z" fill="#1d4f7a"/><path d="M12 7a4 4 0 0 0-4 4c0 3 4 8 4 8s4-5 4-8a4 4 0 0 0-4-4z" fill="#fff"/></svg>
      <div>1274 Lind Avenue<br>Springfield, OR 97477</div>
    </div>
    <div class="item">
      <svg viewBox="0 0 24 26"><path d="M12 1l11 6v12l-11 6-11-6V7z" fill="#1d4f7a"/><path d="M8 8l2-1 2 3-1.5 1.5a8 8 0 0 0 3 3L15 13l3 2-1 2c-5 0-9-4-9-9z" fill="#fff"/></svg>
      <div><strong>Phone</strong><br>+1 (555) 481-2960</div>
    </div>
    <div class="item">
      <svg viewBox="0 0 24 26"><path d="M12 1l11 6v12l-11 6-11-6V7z" fill="#1d4f7a"/><rect x="6" y="9" width="12" height="8" fill="#fff"/><path d="M6 9l6 5 6-5" fill="none" stroke="#1d4f7a" stroke-width="1"/></svg>
      <div><strong>Email</strong><br>hello@kelmora.com</div>
    </div>
  </div>
</section>

<footer class="site-footer">
  <div class="footer-main">
    <div class="brand"><span class="mark"></span>Kelmora</div>
    <ul class="footer-links">
      <li>Home</li><li>Services</li><li>Solutions</li><li>Our Experience</li><li>News</li><li>Contact</li>
    </ul>
    <div class="footer-social"><span></span><span></span><span></span><span></span></div>
  </div>
  <div class="copyright">Copyright &copy; 2024 Kelmora Services. All rights reserved.</div>
</footer>

</body>
</html>
```